Assorted Banner Ads

Create standard sized banner ads (300x250, 728x90, 160x600) using logo and create exciting ads using collateral provided and your own ideas.

```html
<!DOCTYPE html>
<html lang="en">
<head>
<meta charset="utf-8">
<title>Harbor Point Room Escape – Banner Set</title>
<link rel="stylesheet" href="https://fonts.googleapis.com/css2?family=Cinzel:wght@700&family=Montserrat:wght@600;700;800&family=Lexend:wght@500;600&display=swap">
<style>
  :root {
    --page: #3a2a20;
    --parchment: #ebe3ca;
    --parchment-dark: #d8ccaa;
    --green: #2f8a4c;
    --green-light: #7cc894;
    --green-deep: #1e6b36;
    --ink: #2a2a22;
    --photo-dark: #3e1c0a;
    --photo-mid: #8a4418;
    --photo-light: #d4883c;
    --white: #ffffff;
  }
  * { margin: 0; padding: 0; box-sizing: border-box; }
  html, body { width: 1200px; height: 1200px; overflow: hidden; }
  body { background: var(--page); position: relative; font-family: "Montserrat", sans-serif; }

  .banner { position: absolute; overflow: hidden; box-shadow: 0 4px 14px rgba(0,0,0,.45); }
  .banner svg.backdrop { position: absolute; inset: 0; width: 100%; height: 100%; }
  .layer { position: absolute; }

  .brand { position: absolute; text-align: center; color: var(--ink); font-family: "Montserrat", sans-serif; font-weight: 600; line-height: 1.15; }
  .brand-mark { display: block; margin: 0 auto 6px; background: var(--green); }
  .brand-name { display: block; letter-spacing: .08em; }
  .brand-sub { display: block; letter-spacing: .22em; }

  .headline-top { font-family: "Cinzel", serif; font-weight: 700; color: var(--white); letter-spacing: .06em; text-shadow: 2px 2px 3px rgba(0,0,0,.7); white-space: nowrap; }
  .headline-main { font-family: "Montserrat", sans-serif; font-weight: 800; color: var(--white); text-shadow: 2px 2px 4px rgba(0,0,0,.75); white-space: nowrap; }
  .tagline { font-family: "Montserrat", sans-serif; font-weight: 800; color: var(--white); letter-spacing: .04em; text-shadow: 1px 1px 3px rgba(0,0,0,.8); white-space: nowrap; }

  .room-list { list-style: none; font-family: "Lexend", sans-serif; font-weight: 600; color: var(--white); text-shadow: 1px 1px 2px rgba(0,0,0,.8); }
  .room-list li { display: flex; align-items: center; white-space: nowrap; }
  .room-list li::before { content: ""; display: inline-block; background: var(--green); margin-right: .45em; width: .7em; height: .7em; flex: none; }

  .cta { position: absolute; display: flex; align-items: center; justify-content: center; border-radius: 7px;
    background: linear-gradient(180deg, var(--green-light) 0%, var(--green) 55%, var(--green-deep) 100%);
    color: var(--ink); font-family: "Montserrat", sans-serif; font-weight: 600; letter-spacing: .02em;
    box-shadow: 0 2px 3px rgba(0,0,0,.3); white-space: nowrap; }
  .site-url { position: absolute; text-align: center; color: var(--green); font-family: "Montserrat", sans-serif; font-weight: 700; white-space: nowrap; }

  .leaderboard { left: 43px; top: 94px; width: 1113px; height: 137px; }
  .skyscraper { left: 43px; top: 274px; width: 224px; height: 838px; }
  .rectangle { left: 342px; top: 279px; width: 664px; height: 554px; }
</style>
</head>
<body>

<section class="banner leaderboard">
  <svg class="backdrop" viewBox="0 0 1113 137" preserveAspectRatio="none">
    <defs>
      <linearGradient id="lbPhoto" x1="0" y1="0" x2="1" y2="0">
        <stop offset="0" stop-color="var(--photo-dark)"/>
        <stop offset=".45" stop-color="var(--photo-mid)"/>
        <stop offset=".7" stop-color="var(--photo-light)"/>
        <stop offset="1" stop-color="var(--photo-dark)"/>
      </linearGradient>
      <linearGradient id="lbGreen" x1="0" y1="0" x2="0" y2="1">
        <stop offset="0" stop-color="var(--green)"/>
        <stop offset=".5" stop-color="var(--green-light)"/>
        <stop offset="1" stop-color="var(--green)"/>
      </linearGradient>
    </defs>
    <rect width="1113" height="137" fill="url(#lbPhoto)" role="img" aria-label="Photo of a candle-lit wooden ship cabin escape room"/>
    <path d="M0 0 H205 Q240 68 205 137 H0Z" fill="var(--parchment)"/>
    <path d="M196 0 Q236 68 196 137" fill="none" stroke="url(#lbGreen)" stroke-width="12"/>
    <path d="M1113 0 H872 Q836 68 872 137 H1113Z" fill="var(--parchment)"/>
    <path d="M880 0 Q841 68 880 137" fill="none" stroke="url(#lbGreen)" stroke-width="12"/>
  </svg>
  <div class="brand" style="left:18px; top:26px; width:170px;">
    <span class="brand-mark" style="width:22px;height:22px;"></span>
    <span class="brand-name" style="font-size:17px;">HARBOR POINT</span>
    <span class="brand-sub" style="font-size:10px;">ROOM ESCAPE</span>
  </div>
  <div class="layer headline-top" style="left:229px; top:12px; font-size:33px;">Can You Escape</div>
  <div class="layer headline-main" style="left:229px; top:48px; font-size:41px;">IN 60 MINUTES?</div>
  <div class="layer tagline" style="left:230px; top:105px; font-size:17px;">FIND CLUES!&nbsp; SOLVE PUZZLES!</div>
  <ul class="layer room-list" style="left:608px; top:22px; font-size:15.5px; line-height:22px;">
    <li>The Captain's Log</li>
    <li>Sunken Gold Chase</li>
    <li>Island Cell Block</li>
    <li>Neon Nights</li>
  </ul>
  <div class="cta" style="left:897px; top:46px; width:190px; height:35px; font-size:18px;">ESCAPE NOW</div>
  <div class="site-url" style="left:880px; top:91px; width:222px; font-size:10.5px;">www.harborpointescape.com</div>
</section>

<section class="banner skyscraper">
  <svg class="backdrop" viewBox="0 0 224 838" preserveAspectRatio="none">
    <defs>
      <linearGradient id="skPhoto" x1="0" y1="0" x2="0" y2="1">
        <stop offset="0" stop-color="var(--photo-mid)"/>
        <stop offset=".4" stop-color="var(--photo-light)"/>
        <stop offset=".75" stop-color="var(--photo-mid)"/>
        <stop offset="1" stop-color="var(--photo-dark)"/>
      </linearGradient>
      <linearGradient id="skGreen" x1="0" y1="0" x2="1" y2="0">
        <stop offset="0" stop-color="var(--green)"/>
        <stop offset=".5" stop-color="var(--green-light)"/>
        <stop offset="1" stop-color="var(--green)"/>
      </linearGradient>
    </defs>
    <rect width="224" height="838" fill="url(#skPhoto)" role="img" aria-label="Photo of a candle-lit wooden ship cabin escape room"/>
    <path d="M0 0 H224 V150 Q112 270 0 150Z" fill="var(--parchment)"/>
    <path d="M0 150 Q112 270 224 150" fill="none" stroke="url(#skGreen)" stroke-width="10"/>
    <path d="M0 686 Q112 558 224 686 V838 H0Z" fill="var(--parchment)"/>
    <path d="M0 686 Q112 558 224 686" fill="none" stroke="url(#skGreen)" stroke-width="10"/>
  </svg>
  <div class="brand" style="left:0; top:48px; width:224px;">
    <span class="brand-mark" style="width:28px;height:28px;"></span>
    <span class="brand-name" style="font-size:20px;">HARBOR POINT</span>
    <span class="brand-sub" style="font-size:12px;">ROOM ESCAPE</span>
  </div>
  <div class="layer headline-top" style="left:0; top:274px; width:224px; text-align:center; font-size:27px; line-height:35px;">Can You<br>Escape</div>
  <div class="layer headline-main" style="left:0; top:354px; width:224px; text-align:center; font-size:36px; line-height:44px;">IN 60<br>MINUTES?</div>
  <ul class="layer room-list" style="left:14px; top:472px; font-size:13px; line-height:18.5px;">
    <li>The Captain's Log</li>
    <li>Sunken Gold Chase</li>
    <li>Island Cell Block</li>
    <li>Neon Nights</li>
  </ul>
  <div class="layer tagline" style="left:0; top:564px; width:224px; text-align:center; font-size:15px; line-height:21px;">FIND CLUES!<br>SOLVE PUZZLES!</div>
  <div class="cta" style="left:23px; top:743px; width:173px; height:33px; font-size:16px;">ESCAPE NOW</div>
  <div class="site-url" style="left:0; top:788px; width:224px; font-size:9.5px;">www.harborpointescape.com</div>
</section>

<section class="banner rectangle">
  <svg class="backdrop" viewBox="0 0 664 554" preserveAspectRatio="none">
    <defs>
      <radialGradient id="mrPhoto" cx=".5" cy=".5" r=".7">
        <stop offset="0" stop-color="var(--photo-light)"/>
        <stop offset=".55" stop-color="var(--photo-mid)"/>
        <stop offset="1" stop-color="var(--photo-dark)"/>
      </radialGradient>
      <linearGradient id="mrGreen" x1="0" y1="0" x2="1" y2="0">
        <stop offset="0" stop-color="var(--green)"/>
        <stop offset=".5" stop-color="var(--green-light)"/>
        <stop offset="1" stop-color="var(--green)"/>
      </linearGradient>
    </defs>
    <rect width="664" height="554" fill="url(#mrPhoto)" role="img" aria-label="Photo of a candle-lit wooden ship cabin escape room"/>
    <path d="M0 0 H664 V93 Q332 285 0 93Z" fill="var(--parchment)"/>
    <path d="M0 93 Q332 285 664 93" fill="none" stroke="url(#mrGreen)" stroke-width="11"/>
    <path d="M0 492 Q332 444 664 492 V554 H0Z" fill="var(--parchment)"/>
    <path d="M0 492 Q332 444 664 492" fill="none" stroke="url(#mrGreen)" stroke-width="11"/>
  </svg>
  <div class="brand" style="left:0; top:52px; width:664px;">
    <span class="brand-mark" style="width:30px;height:30px;"></span>
    <span class="brand-name" style="font-size:26px;">HARBOR POINT</span>
    <span class="brand-sub" style="font-size:15px;">ROOM ESCAPE</span>
  </div>
  <div class="layer headline-top" style="left:84px; top:205px; font-size:47px;">Can You Escape</div>
  <div class="layer headline-main" style="left:84px; top:260px; font-size:56px;">IN 60 MINUTES?</div>
  <ul class="layer room-list" style="left:80px; top:342px; font-size:17.5px; line-height:24px;">
    <li>The Captain's Log</li>
    <li>Sunken Gold Chase</li>
  </ul>
  <ul class="layer room-list" style="left:367px; top:342px; font-size:17.5px; line-height:24px;">
    <li>Island Cell Block</li>
    <li>Neon Nights</li>
  </ul>
  <div class="layer tagline" style="left:0; top:403px; width:664px; text-align:center; font-size:19px;">FIND CLUES! SOLVE PUZZLES!</div>
  <div class="cta" style="left:191px; top:445px; width:273px; height:49px; font-size:26px;">ESCAPE NOW</div>
  <div class="site-url" style="left:0; top:503px; width:664px; font-size:26px;">www.harborpointescape.com</div>
</section>

</body>
</html>
```